Most captivating card ever!

Life Coach - Professional Adventurer - Entrepreneur
I need the worlds most amazing business card for my personal brand. This business card will mostly be used to give to prospective clients for life coaching and business coaching.
Be creative, be adventurous. It needs to stand out. Make people say.. I need this guy!
My background is as an entrepreneur and professional adventurer undertaking extreme expeditions. I am now moving into life coaching.
No specific design ideas, so you have full creativity. Show me your best.
Industry/Entity Type
Life Coaching
Contact Information for Business Card
Mark Dellow
meetmark.com.au
0458260913
Colors
Designer to choose colors to be used in the design.
Look and feel

```html
<!DOCTYPE html>
<html lang="en">
<head>
<meta charset="utf-8">
<title>Business card – front and back</title>
<link rel="stylesheet" href="https://fonts.googleapis.com/css2?family=Poppins:wght@300;400;500&display=swap">
<style>
  :root {
    --backdrop: #2b2d2d;
    --card: #ffffff;
    --green: #17943c;
    --green-light: #2fae4e;
  }
  * { box-sizing: border-box; margin: 0; padding: 0; }
  html, body {
    width: 1200px; height: 1200px; overflow: hidden;
    background: var(--backdrop);
    font-family: "Poppins", sans-serif;
  }
  .stage {
    position: relative; width: 1200px; height: 1200px;
    display: flex; align-items: center; justify-content: center; gap: 80px;
  }
  .card {
    width: 450px; height: 740px;
    background: var(--card);
    box-shadow: 0 10px 30px rgba(0,0,0,.45);
    display: flex; flex-direction: column; align-items: center;
    color: var(--green); text-align: center;
  }
  .brand {
    font-weight: 500; font-size: 44px; line-height: 1.1;
    color: var(--green); letter-spacing: .5px;
  }
  .card--front .brand { margin-top: 150px; }
  .card--back .brand { margin-top: 190px; }
  .person { margin-top: 80px; }
  .person__name { font-weight: 400; font-size: 34px; line-height: 1.1; }
  .person__role {
    font-weight: 300; font-size: 20px; letter-spacing: 8px;
    color: var(--green-light); margin-top: 4px;
  }
  .contact { margin-top: 36px; font-size: 20px; line-height: 1.35; font-weight: 400; }
  .contact__icons { display: flex; gap: 10px; justify-content: center; margin-bottom: 10px; }
  .contact__icons svg { width: 22px; height: 22px; }
  .roles { font-weight: 500; font-size: 28px; line-height: 1.25; }
  .card--front .roles { margin-top: 44px; }
  .card--back .roles { margin-top: 210px; }
</style>
</head>
<body>
<main class="stage">
  <section class="card card--front">
    <div class="brand">Summit Coaching</div>
    <div class="person">
      <div class="person__name">Mark Dellow</div>
      <div class="person__role">Life Coach</div>
    </div>
    <div class="contact">
      <div class="contact__icons">
        <svg viewBox="0 0 24 24" aria-hidden="true">
          <circle cx="12" cy="12" r="12" fill="var(--green)"/>
          <path d="M8 6.5l2 .2 1 2.6-1.3 1.1a7 7 0 0 0 3.9 3.9l1.1-1.3 2.6 1-.1 2a1.5 1.5 0 0 1-1.6 1.3A10 10 0 0 1 6.7 8.1 1.5 1.5 0 0 1 8 6.5z" fill="#fff"/>
        </svg>
        <svg viewBox="0 0 24 24" aria-hidden="true">
          <circle cx="12" cy="12" r="12" fill="var(--green)"/>
          <circle cx="12" cy="12" r="6" fill="none" stroke="#fff" stroke-width="1.4"/>
          <path d="M6 12h12M12 6c-2.5 3-2.5 9 0 12M12 6c2.5 3 2.5 9 0 12" fill="none" stroke="#fff" stroke-width="1.2"/>
        </svg>
      </div>
      <div class="contact__phone">0458260913</div>
      <div class="contact__web">meetmark.com.au</div>
    </div>
    <div class="roles">
      <div>Life Coach</div>
      <div>Professional Adventurer</div>
      <div>Entrepreneur</div>
    </div>
  </section>

  <section class="card card--back">
    <div class="brand">Summit Coaching</div>
    <div class="roles">
      <div>Life Coach</div>
      <div>Professional Adventurer</div>
      <div>Entrepreneur</div>
    </div>
  </section>
</main>
</body>
</html>
```